****Business Card Design for Cormwell Development. Design based around attached logo/company name

I’m looking for business card design for my company Cormwell Development Group,LLC. Design should be professional, sharp and minimal. Outside of the attached logos, greyscale colors for remainder of cards. My thoughts are two-sided card with attached logo on one side and my info on the other but open to one-sided as well with right design.
Target Market(s)
Real estate professionals including banks, private investors, property owners, developers, commercial tenants like Brewlantic, Granvey or Tamsett’s.
Industry/Entity Type
Commercial real estate development and investments.
Contact Information for Business Card
Name, title, email, phone #’s, web address and physical address
Font styles to use
Other font styles liked:
- Helvetica, Garamond, etc
Colors
Designer to choose only greyscale colors for use in the design.
Requirements
Must have
- Attached logo first or second options.
Nice to have
- Two sided card with logo on one side. Attached Logo/company name can be laid out any way that flows as long as it’s legible.name
Should not have
- No loud colors. ***Please do not include logo, I have removed the company design with a logo image.

```html
<!DOCTYPE html>
<html lang="en">
<head>
<meta charset="utf-8">
<title>Cormwell Development Group, LLC — Business Card</title>
<link rel="stylesheet" href="https://fonts.googleapis.com/css2?family=Cinzel:wght@400&family=Tinos:wght@400&display=swap">
<style>
  :root {
    --backdrop: #2c2c2d;
    --card-top: #232427;
    --card-bottom: #1c1d20;
    --brand-grey: #6c6f7b;
    --text-grey: #8b8e98;
    --muted-grey: #7d808a;
    --band-grey: #5b5f6d;
    --band-text: #e4e5ea;
  }
  * { margin: 0; padding: 0; box-sizing: border-box; }
  html, body { width: 1200px; height: 1138px; overflow: hidden; }
  body { background: var(--backdrop); position: relative; font-family: "Tinos", "Times New Roman", serif; }

  .card {
    position: absolute;
    border-radius: 16px;
    overflow: hidden;
    background: linear-gradient(160deg, var(--card-top), var(--card-bottom));
    box-shadow: 0 6px 14px rgba(0,0,0,.45);
  }
  .card--front { left: 272px; top: 184px; width: 624px; height: 376px; }
  .card--back  { left: 274px; top: 606px; width: 620px; height: 375px; }

  .wordmark { position: absolute; color: var(--brand-grey); font-family: "Cinzel", "Times New Roman", serif; }
  .wordmark__name { display: block; line-height: 1; letter-spacing: .02em; padding-bottom: 4px; border-bottom: 1px solid var(--brand-grey); }
  .wordmark__sub { display: block; line-height: 1; letter-spacing: .14em; }

  .card--front .wordmark { left: 45px; top: 112px; }
  .card--front .wordmark__name { font-size: 43px; }
  .card--front .wordmark__sub { font-size: 15px; margin-top: 6px; }

  .card--back .wordmark { left: 24px; top: 52px; }
  .card--back .wordmark__name { font-size: 55px; }
  .card--back .wordmark__sub { font-size: 21px; margin-top: 8px; }

  .person { position: absolute; left: 24px; top: 226px; color: var(--muted-grey); }
  .person__name { font-family: "Cinzel", "Times New Roman", serif; font-size: 23px; color: var(--text-grey); letter-spacing: .02em; line-height: 1; }
  .person__title { font-size: 16px; margin-top: 8px; }
  .person__address { font-size: 16px; line-height: 23px; margin-top: 32px; }

  .contact { position: absolute; left: 352px; top: 222px; list-style: none; color: var(--muted-grey); font-size: 16px; }
  .contact li { display: flex; align-items: center; height: 22.5px; }
  .contact svg { width: 14px; height: 12px; margin-right: 10px; fill: var(--band-text); opacity: .85; }

  .band { position: absolute; left: 0; bottom: 0; width: 100%; height: 48px; }
  .band__text { position: absolute; right: 30px; bottom: 16px; font-size: 17px; color: var(--band-text); }
</style>
</head>
<body>

<section class="card card--front" aria-label="Card front">
  <div class="wordmark">
    <span class="wordmark__name">CORMWELL</span>
    <span class="wordmark__sub">DEVELOPMENT GROUP, LLC</span>
  </div>
</section>

<section class="card card--back" aria-label="Card back">
  <div class="wordmark">
    <span class="wordmark__name">CORMWELL</span>
    <span class="wordmark__sub">DEVELOPMENT GROUP, LLC</span>
  </div>

  <div class="person">
    <p class="person__name">JOHN DOE SMITH</p>
    <p class="person__title">Managing Director</p>
    <p class="person__address">234 Anywhere St., Any City,<br>Any Town, US 123456</p>
  </div>

  <ul class="contact">
    <li><svg viewBox="0 0 14 12"><path d="M1 4c0-2 3-3 6-3s6 1 6 3v1h-3V4H4v1H1zM3 6h8l2 5H1z"/></svg>828-111-1111</li>
    <li><svg viewBox="0 0 14 12"><path d="M1 2h12v8H1zM2 3v.5l5 3.5 5-3.5V3zm0 2v4h10V5L7 8.5z" fill-rule="evenodd"/></svg>john@yourwebsite.com</li>
    <li><svg viewBox="0 0 14 12"><circle cx="7" cy="6" r="5.5"/></svg>www.yourwebsite.com</li>
  </ul>

  <svg class="band" viewBox="0 0 620 48" preserveAspectRatio="none" aria-hidden="true">
    <path d="M0 33H332L352 0H610Q620 0 620 10V48H0Z" fill="var(--band-grey)"/>
  </svg>
  <p class="band__text">Cormwell Development Group, LLC</p>
</section>

</body>
</html>
```